Business Card Design Project - Nerd Crew

High quality business card Must be funky.

We are an IT support from home and office, but our image is more retro.

Our logo is black and lime green. IT should be a 2 sided card with the multiple coloured ties somehow used on the reverse side (be creative!)

Black or white background fine or a combo of both

Target Market(s)

consumer and business

Industry/Entity Type

Business

```html
<!DOCTYPE html>
<html lang="en">
<head>
<meta charset="utf-8">
<title>Nerd Crew – Business Card</title>
<link href="https://fonts.googleapis.com/css2?family=Noto+Serif:ital,wght@0,700;1,400;1,700&display=swap" rel="stylesheet">
<style>
  :root {
    --backdrop: #e9e6e1;
    --card-dark: #2a2a2c;
    --card-dark-soft: #343436;
    --panel-grey: #6b6b6d;
    --panel-grey-deep: #5e5e60;
    --ink-white: #f4f4f4;
    --ink-dark: #2b2b2b;
    --lime: #8cc63f;
    --pink: #ec5f97;
    --cyan: #1fb5d3;
    --red: #e0393e;
    --text-light: #f1f1f1;
  }
  * { box-sizing: border-box; margin: 0; padding: 0; }
  html, body { width: 1200px; height: 900px; overflow: hidden; }
  body {
    background: var(--backdrop);
    font-family: "Noto Serif", Georgia, serif;
    position: relative;
  }
  .card {
    position: absolute;
    top: 82px;
    width: 420px;
    height: 736px;
    background: var(--card-dark);
    overflow: hidden;
    box-shadow: 0 6px 18px rgba(0,0,0,0.18);
  }
  .card--back { left: 150px; }
  .card--front { left: 630px; }

  .tie-pattern {
    position: absolute;
    inset: 0;
    background: linear-gradient(160deg, var(--card-dark-soft), var(--card-dark));
  }

  .wordmark {
    position: absolute;
    left: 0; right: 0;
    text-align: center;
    font-family: "Noto Serif", Georgia, serif;
    font-weight: 700;
    font-style: normal;
    font-size: 60px;
    letter-spacing: -1px;
    color: var(--ink-white);
    display: flex;
    justify-content: center;
    align-items: center;
    gap: 16px;
  }
  .wordmark__dot {
    width: 16px; height: 16px;
    border-radius: 50%;
    background: var(--lime);
  }
  .card--back .wordmark { bottom: 92px; }
  .card--front .wordmark { top: 100px; }

  .tie-cluster {
    position: absolute;
    left: 70px;
    top: 70px;
    width: 290px;
    height: 330px;
    border-radius: 10px;
    background: linear-gradient(200deg,
      rgba(140,198,63,0.55) 0%,
      rgba(236,95,151,0.5) 35%,
      rgba(224,57,62,0.45) 60%,
      rgba(31,181,211,0.5) 100%);
  }

  .contact-panel {
    position: absolute;
    left: 0; right: 0;
    top: 268px;
    bottom: 0;
    background: linear-gradient(180deg, var(--panel-grey), var(--panel-grey-deep));
    padding: 44px 34px 0 34px;
  }
  .person__name {
    font-weight: 700;
    font-style: italic;
    font-size: 30px;
    color: var(--ink-dark);
  }
  .person__role {
    font-style: italic;
    font-size: 17px;
    color: var(--lime);
    margin-top: 2px;
  }
  .contact-list {
    list-style: none;
    margin-top: 64px;
    text-align: right;
  }
  .contact-list__item {
    display: flex;
    justify-content: flex-end;
    align-items: center;
    gap: 10px;
    font-style: italic;
    font-size: 17px;
    color: var(--text-light);
    line-height: 30px;
  }
  .contact-list__icon { width: 16px; height: 16px; flex: none; }
  .website {
    margin-top: 34px;
    text-align: right;
    font-weight: 700;
    font-style: italic;
    font-size: 30px;
    color: var(--text-light);
    padding-right: 26px;
  }
</style>
</head>
<body>

  <section class="card card--back" aria-label="Card reverse">
    <div class="tie-pattern" role="img" aria-label="Repeating pattern of dark grey neckties"></div>
    <div class="tie-cluster" role="img" aria-label="Illustration of lime, pink, red, dotted green and cyan neckties"></div>
    <div class="wordmark"><span>Nerd Crew</span><span class="wordmark__dot"></span></div>
  </section>

  <section class="card card--front" aria-label="Card front">
    <div class="tie-pattern" role="img" aria-label="Repeating pattern of dark grey neckties"></div>
    <div class="wordmark"><span>Nerd Crew</span><span class="wordmark__dot"></span></div>

    <div class="contact-panel">
      <p class="person__name">Daniel K. Morrow</p>
      <p class="person__role">Art Director</p>

      <ul class="contact-list">
        <li class="contact-list__item">
          <span>DanielKMorrow@nerdcrew.com</span>
          <svg class="contact-list__icon" viewBox="0 0 16 16" aria-hidden="true">
            <rect x="1" y="3" width="14" height="10" rx="1.5" fill="var(--pink)"/>
            <path d="M1.5 4 L8 9 L14.5 4" fill="none" stroke="var(--panel-grey)" stroke-width="1.4"/>
          </svg>
        </li>
        <li class="contact-list__item">
          <span>001-555-0142</span>
          <svg class="contact-list__icon" viewBox="0 0 16 16" aria-hidden="true">
            <path d="M3 1.5 L6 1.5 L7 5 L5.3 6.3 C6.2 8.3 7.7 9.8 9.7 10.7 L11 9 L14.5 10 L14.5 13 C14.5 14 13.6 14.7 12.6 14.5 C7 13.6 2.4 9 1.5 3.4 C1.3 2.4 2 1.5 3 1.5 Z" fill="var(--pink)"/>
          </svg>
        </li>
        <li class="contact-list__item">
          <span>001-555-0142</span>
          <svg class="contact-list__icon" viewBox="0 0 16 16" aria-hidden="true">
            <rect x="4" y="1" width="8" height="14" rx="1.5" fill="var(--pink)"/>
            <rect x="5.3" y="2.8" width="5.4" height="8" fill="var(--panel-grey)"/>
            <circle cx="8" cy="13" r="0.9" fill="var(--panel-grey)"/>
          </svg>
        </li>
      </ul>

      <p class="website">www.nerdcrew.asia</p>
    </div>
  </section>

</body>
</html>
```